Successful Software Co Launching A Super FUN Mobile & Web Application - ROCKSTAR Designer Needed

Our App is called "Brightly Tally"It is an employee "gamification" app designed to make working at your job fun...Employees complete simple tasks throughout the work day and are rewarded with points they can redeem for different gifts and benefits...We an AMAZING User Interface designed for both the mobile app and website app. We are looking for a clean, modern and simple design... This app is designed to make employees more engaged at work while having fun doing the things they already do each day...They can then redeem their points for rewards. It needs to be easy to understand and simple in its design...Example: A local carpet cleaning business uses our app.Their employees show up to work on time - They get 50 pointsThey clean out their work vehicle - They get 100 pointsThey up-sell an additional cleaning job - The get 250 pointsEtc...The app will also have fun icons and graphics that appear on the screen when an employee accomplishes a task.The app will play fun music sounds when they accomplish tasks too.
Updates

Need extra days to review

Target Market(s)

Small business owners

Logo Text

Brightly Tally

Font styles to use
Sans Serif

Colors

Designer to choose colors to be used in the design.

Requirements
Must have
• Simple elegant design
Nice to have
• I'd like to see examples of fun "icons" that could pop up on the screen after an employee completes a "task" and earns points... Something fun to pop up on the screen... (like a happy face, a thumbs up, fun text bubbles... "Way To Go!" etc... or any other fun ideas)

```html
<!DOCTYPE html>
<html lang="en">
<head>
<meta charset="utf-8">
<title>Brightly Tally – App Screens</title>
<link rel="stylesheet" href="https://fonts.googleapis.com/css2?family=Mulish:wght@400;600;700;800&family=Montserrat:wght@500&display=swap">
<style>
:root{
  --blue:#1634f2;
  --blue-soft:#e7e4fb;
  --ink:#111322;
  --muted:#6b6f80;
  --line:#e8e9f2;
  --page:#f6f7fc;
  --white:#ffffff;
  --red:#e53935;
  --pale:#d9dcfb;
}
*{box-sizing:border-box;margin:0;padding:0}
html,body{width:1200px;height:2296px;overflow:hidden}
body{background:var(--page);font-family:"Mulish",sans-serif;color:var(--ink);position:relative}
.screen{position:absolute;width:246px;height:525px;background:var(--white);border-radius:22px;box-shadow:0 10px 30px rgba(22,52,242,.12);overflow:hidden}
.label{position:absolute;width:246px;text-align:center;font-family:"Montserrat",sans-serif;font-weight:500;font-size:20px;letter-spacing:2px;color:var(--ink)}
.abs{position:absolute}
.brand-mini{position:absolute;top:34px;left:0;width:100%;display:flex;justify-content:center;align-items:center;gap:4px;font-weight:800;font-size:9px;color:var(--blue)}
.brand-mini i{width:10px;height:10px;border-radius:50%;background:var(--blue);display:block}
.btn{position:absolute;left:65px;width:115px;height:34px;border-radius:4px;background:var(--blue);color:var(--white);font-weight:700;font-size:9px;letter-spacing:1px;display:flex;align-items:center;justify-content:center;box-shadow:0 4px 10px rgba(22,52,242,.25)}
.btn.ghost{background:var(--white);color:var(--blue);box-shadow:0 4px 12px rgba(20,30,80,.1)}
.field{position:absolute;left:15px;width:216px;height:28px;border-radius:4px;background:var(--white);box-shadow:0 3px 10px rgba(20,30,80,.09);font-size:9px;padding-left:9px;display:flex;align-items:center;justify-content:space-between;padding-right:10px}
.title{position:absolute;left:15px;font-weight:700;font-size:13px;line-height:1.3}
.small{font-size:8px}
.center{left:0;width:100%;text-align:center}
.social{position:absolute;top:434px;width:43px;height:23px;border-radius:3px;color:var(--white);font-size:7px;font-weight:700;display:flex;align-items:center;justify-content:center}
.social.a{left:44px;background:#3b5a9a}
.social.b{left:128px;background:#1da1f2}
.link{color:var(--blue);font-weight:700}
.hamb{position:absolute;left:15px;top:44px}
.bell{position:absolute;right:15px;top:41px}
.bar{position:absolute;left:15px;top:140px;width:214px;height:28px;border-radius:14px;background:var(--blue-soft)}
.bar span{position:absolute;left:0;top:0;height:28px;width:161px;border-radius:14px;background:var(--blue);color:var(--white);font-size:9px;display:flex;align-items:center;justify-content:flex-end;padding-right:20px}
.row-head{position:absolute;left:15px;width:216px;display:flex;justify-content:space-between;align-items:baseline;font-weight:700;font-size:10px}
.row-head a{font-size:7px;color:var(--blue);font-weight:600}
.card{position:absolute;left:15px;width:216px;border-radius:5px;background:var(--white);box-shadow:0 4px 14px rgba(20,30,80,.1)}
.reward-brand{position:absolute;left:8px;top:10px;display:flex;align-items:center;gap:4px;font-size:8px;font-weight:700;color:var(--ink)}
.reward-brand i{width:14px;height:14px;border-radius:50%;background:var(--ink);display:block}
.reward-text{position:absolute;left:8px;font-size:12px;font-weight:600;line-height:1.3}
.reward-text b{color:var(--blue);font-weight:600}
.redeem{position:absolute;right:8px;width:48px;height:16px;border-radius:2px;background:var(--blue);color:var(--white);font-size:7px;font-weight:700;display:flex;align-items:center;justify-content:center;letter-spacing:.5px}
.redeem.off{background:var(--pale);color:var(--white)}
.hist{position:absolute;left:15px;width:216px;height:43px;border-radius:4px;background:var(--white);box-shadow:0 3px 10px rgba(20,30,80,.09);font-size:8px}
.hist p{position:absolute;left:7px;top:8px}
.hist em{position:absolute;right:8px;bottom:8px;font-style:normal;font-size:9px}
.hist em b{color:var(--blue);font-weight:600}
.dots{position:absolute;left:0;width:100%;display:flex;justify-content:center;gap:3px}
.dots i{display:block;width:9px;height:2px;background:var(--line)}
.dots i:first-child{background:var(--blue)}
.nav{position:absolute;left:0;bottom:0;width:100%;height:45px;border-top:1px solid var(--line);display:flex;justify-content:space-around;align-items:center}
.nav div{display:flex;flex-direction:column;align-items:center;font-size:7px;color:var(--blue);font-weight:600;gap:2px;width:60px}
.menu-item{position:absolute;left:15px;width:216px;font-size:8px;padding-bottom:6px;border-bottom:1px solid var(--line)}
.avatar{position:absolute;left:15px;top:117px;width:90px;height:100px;border-radius:3px;background:linear-gradient(135deg,#cfcfcf,#5a5a5a)}
</style>
</head>
<body>

<!-- Welcome -->
<section class="screen" style="left:117px;top:80px">
  <div class="abs center" style="top:150px;display:flex;flex-direction:column;align-items:center;gap:10px">
    <i style="width:46px;height:46px;border-radius:50%;background:var(--blue);display:block"></i>
    <span style="font-weight:700;font-size:13px;color:var(--blue);line-height:1.3;text-align:center">Brightly<br>Tally</span>
  </div>
  <div class="btn" style="top:340px">LOGIN</div>
  <div class="btn ghost" style="top:392px">SIGN UP</div>
  <p class="abs center small" style="top:496px;color:var(--blue);font-size:7px">Terms and conditions - Privacy</p>
</section>
<p class="label" style="left:117px;top:643px">Welcome</p>

<!-- Login -->
<section class="screen" style="left:480px;top:80px">
  <div class="brand-mini"><i></i>Brightly Tally</div>
  <h1 class="title" style="top:88px">Welcome,<br>Please login to continue!</h1>
  <div class="field" style="top:140px">User Name</div>
  <div class="field" style="top:180px">Password
    <svg width="10" height="6" viewBox="0 0 10 6"><path d="M1 1 Q5 5 9 1" fill="none" stroke="#1634f2" stroke-width="1.2"/></svg></div>
  <p class="abs small link" style="top:228px;right:15px;font-weight:600;font-size:7px">Forgot password?</p>
  <div class="btn" style="top:315px">LOGIN</div>
  <p class="abs center small" style="top:388px;color:var(--blue);font-size:7px">OR</p>
  <p class="abs center small" style="top:412px;font-size:7px">Continue using socials</p>
  <div class="social a">Circlo</div><div class="social b">Chirpa</div>
  <p class="abs center small" style="top:496px;color:var(--muted);font-size:7px">Don't have an account? <span class="link">Sign up</span></p>
</section>
<p class="label" style="left:480px;top:643px">Login</p>

<!-- Signup -->
<section class="screen" style="left:843px;top:80px">
  <div class="brand-mini"><i></i>Brightly Tally</div>
  <h1 class="title" style="top:88px">Welcome,<br>Please login to continue!</h1>
  <div class="field" style="top:140px">User Name</div>
  <div class="field" style="top:180px">Email</div>
  <div class="field" style="top:220px">Password
    <svg width="10" height="6" viewBox="0 0 10 6"><path d="M1 1 Q5 5 9 1" fill="none" stroke="#1634f2" stroke-width="1.2"/></svg></div>
  <div class="field" style="top:260px">Confirm password
    <svg width="10" height="6" viewBox="0 0 10 6"><path d="M1 1 Q5 5 9 1" fill="none" stroke="#1634f2" stroke-width="1.2"/></svg></div>
  <div class="btn" style="top:315px">SIGN UP</div>
  <p class="abs center small" style="top:388px;color:var(--blue);font-size:7px">OR</p>
  <p class="abs center small" style="top:412px;font-size:7px">Continue using socials</p>
  <div class="social a">Circlo</div><div class="social b">Chirpa</div>
  <p class="abs center small" style="top:496px;color:var(--muted);font-size:7px">Already have an account? <span class="link">Login</span></p>
</section>
<p class="label" style="left:843px;top:643px">Signup</p>

<!-- Home -->
<section class="screen" style="left:117px;top:847px">
  <svg class="hamb" width="14" height="10" viewBox="0 0 14 10"><path d="M0 1h14M0 5h10M0 9h14" stroke="#1634f2" stroke-width="1.4"/></svg>
  <div class="brand-mini"><i></i>Brightly Tally</div>
  <svg class="bell" width="11" height="13" viewBox="0 0 11 13"><path d="M2 9V5.5a3.5 3.5 0 0 1 7 0V9l1 1.5H1z M4.3 11.5a1.2 1.2 0 0 0 2.4 0" fill="none" stroke="#1634f2" stroke-width="1.1"/></svg>
  <h2 class="title" style="top:86px;font-weight:600">Welcome, Daniel.</h2>
  <p class="abs" style="top:110px;left:15px;font-size:6.5px">You are 900 points away from your next reward.</p>
  <div class="bar"><span>1200/2100</span></div>
  <p class="abs" style="top:176px;right:15px;font-size:7.5px">monthly target: <span class="link">2100</span></p>
  <div class="row-head" style="top:200px">Rewards <a>view all</a></div>
  <div class="card" style="top:214px;height:94px">
    <div class="reward-brand"><i></i>Bean Lane</div>
    <p class="reward-text" style="top:42px"><b>15$</b> Bean Lane card<br>for 900 points</p>
    <div class="redeem" style="top:72px">REDEEM</div>
  </div>
  <div class="dots" style="top:332px"><i></i><i></i><i></i></div>
  <div class="row-head" style="top:354px">History <a>view all</a></div>
  <div class="hist" style="top:372px"><p>Show up on time for 1 month</p><em><b>600</b> points</em></div>
  <div class="hist" style="top:424px"><p>Up-sell 250$ in a service</p><em><b>900</b> points</em></div>
  <nav class="nav">
    <div><svg width="12" height="12" viewBox="0 0 12 12"><path d="M1 6 6 1.5 11 6M2.5 5v6h7V5" fill="none" stroke="#1634f2" stroke-width="1.1"/></svg>HOME</div>
    <div><svg width="12" height="12" viewBox="0 0 12 12"><path d="M1.5 4h9v2.5h-9zM2.5 6.5h7V11h-7zM6 4v7M6 4C4 1 2.5 3 6 4C8 1 9.5 3 6 4" fill="none" stroke="#111322" stroke-width="1"/></svg></div>
    <div><svg width="12" height="12" viewBox="0 0 12 12"><circle cx="6" cy="3.8" r="2.3" fill="none" stroke="#111322" stroke-width="1"/><path d="M1.8 11a4.2 4.2 0 0 1 8.4 0" fill="none" stroke="#111322" stroke-width="1"/></svg></div>
  </nav>
</section>
<p class="label" style="left:117px;top:1409px">Home</p>

<!-- Menu Open -->
<section class="screen" style="left:480px;top:847px">
  <svg class="hamb" width="14" height="10" viewBox="0 0 14 10"><path d="M0 1h14M0 5h10M0 9h14" stroke="#1634f2" stroke-width="1.4"/></svg>
  <div class="brand-mini"><i></i>Brightly Tally</div>
  <svg class="bell" width="11" height="13" viewBox="0 0 11 13"><path d="M2 9V5.5a3.5 3.5 0 0 1 7 0V9l1 1.5H1z M4.3 11.5a1.2 1.2 0 0 0 2.4 0" fill="none" stroke="#1634f2" stroke-width="1.1"/></svg>
  <h2 class="title" style="top:86px;font-weight:600">Welcome, Daniel.</h2>
  <p class="abs" style="top:110px;left:15px;font-size:6.5px">You are 900 points away from your next reward.</p>
  <div class="bar" style="top:137px"><span>1200/2100</span></div>
  <div class="row-head" style="top:192px">Rewards <a>view all</a></div>
  <div class="card" style="top:206px;height:92px">
    <div class="reward-brand"><i></i>Bean Lane</div>
    <p class="reward-text" style="top:40px"><b>15$</b> Bean Lane card<br>for 900 points</p>
    <div class="redeem" style="top:70px">REDEEM</div>
  </div>
  <div class="dots" style="top:322px"><i></i><i></i><i></i></div>
  <div class="row-head" style="top:344px">History <a>view all</a></div>
  <div class="hist" style="top:362px;height:28px"><p>Show up on time for 1 month</p></div>
  <p class="abs small link" style="top:404px;left:15px;font-weight:600">Menu</p>
  <p class="menu-item" style="top:434px">Contact Employer</p>
  <p class="menu-item" style="top:460px;border-color:#9aa6f7">Request time off</p>
  <p class="abs small" style="top:488px;left:15px;color:var(--red)">Log out</p>
</section>
<p class="label" style="left:480px;top:1409px">Menu Open</p>

<!-- Rewards -->
<section class="screen" style="left:843px;top:847px">
  <svg class="hamb" width="14" height="10" viewBox="0 0 14 10"><path d="M0 1h14M0 5h10M0 9h14" stroke="#1634f2" stroke-width="1.4"/></svg>
  <div class="brand-mini"><i></i>Brightly Tally</div>
  <svg class="bell" width="11" height="13" viewBox="0 0 11 13"><path d="M2 9V5.5a3.5 3.5 0 0 1 7 0V9l1 1.5H1z M4.3 11.5a1.2 1.2 0 0 0 2.4 0" fill="none" stroke="#1634f2" stroke-width="1.1"/></svg>
  <h2 class="title" style="top:90px;font-size:11px">Rewards</h2>
  <div class="card" style="top:115px;height:110px">
    <div class="reward-brand"><i></i>Bean Lane</div>
    <p class="reward-text" style="top:44px"><b>15$</b> Bean Lane card<br>for 900 points</p>
    <div class="redeem" style="top:86px">REDEEM</div>
  </div>
  <div class="card" style="top:233px;height:110px">
    <div class="reward-brand" style="font-size:7px"><i style="width:8px;height:8px"></i>Tunely</div>
    <p class="reward-text" style="top:44px"><b>18$</b> Tunely card<br>for 1100 points</p>
    <div class="redeem" style="top:86px">REDEEM</div>
  </div>
  <div class="card" style="top:351px;height:110px">
    <div class="reward-brand"><i style="border-radius:2px"></i>Volt Mart</div>
    <p class="reward-text" style="top:44px">You need 3000 points<br>to unlock this card</p>
    <div class="redeem off" style="top:86px">REDEEM</div>
  </div>
  <nav class="nav">
    <div><svg width="12" height="12" viewBox="0 0 12 12"><path d="M1 6 6 1.5 11 6M2.5 5v6h7V5" fill="none" stroke="#111322" stroke-width="1.1"/></svg></div>
    <div><svg width="12" height="12" viewBox="0 0 12 12"><path d="M1.5 4h9v2.5h-9zM2.5 6.5h7V11h-7zM6 4v7M6 4C4 1 2.5 3 6 4C8 1 9.5 3 6 4" fill="none" stroke="#1634f2" stroke-width="1"/></svg>REWARDS</div>
    <div><svg width="12" height="12" viewBox="0 0 12 12"><circle cx="6" cy="3.8" r="2.3" fill="none" stroke="#111322" stroke-width="1"/><path d="M1.8 11a4.2 4.2 0 0 1 8.4 0" fill="none" stroke="#111322" stroke-width="1"/></svg></div>
  </nav>
</section>
<p class="label" style="left:843px;top:1409px">Rewards</p>

<!-- Profile -->
<section class="screen" style="left:480px;top:1615px">
  <svg class="hamb" width="14" height="10" viewBox="0 0 14 10"><path d="M0 1h14M0 5h10M0 9h14" stroke="#1634f2" stroke-width="1.4"/></svg>
  <div class="brand-mini"><i></i>Brightly Tally</div>
  <svg class="bell" width="11" height="13" viewBox="0 0 11 13"><path d="M2 9V5.5a3.5 3.5 0 0 1 7 0V9l1 1.5H1z M4.3 11.5a1.2 1.2 0 0 0 2.4 0" fill="none" stroke="#1634f2" stroke-width="1.1"/></svg>
  <h2 class="title" style="top:90px;font-size:11px">Profile</h2>
  <div class="avatar" role="img" aria-label="Black and white portrait photo of the employee"></div>
  <p class="abs" style="top:145px;left:111px;font-size:11px;font-weight:600">Daniel Reyes</p>
  <p class="abs" style="top:162px;left:111px;font-size:8px;font-weight:600">Harbor Vale, CA</p>
  <p class="abs" style="top:175px;left:111px;font-size:7px"><span class="link" style="font-weight:600">3000</span> points</p>
  <div class="abs" style="top:189px;left:111px;width:50px;height:15px;background:var(--blue);color:var(--white);font-size:7px;font-weight:700;display:flex;align-items:center;justify-content:center;border-radius:2px">EDIT</div>
  <h3 class="title" style="top:250px;font-size:11px">History</h3>
  <div class="hist" style="top:272px"><p>Show up on time for 1 month</p><em><b>600</b> points</em></div>
  <div class="hist" style="top:324px"><p>Up-sell 250$ in a service</p><em><b>900</b> points</em></div>
  <nav class="nav">
    <div><svg width="12" height="12" viewBox="0 0 12 12"><path d="M1 6 6 1.5 11 6M2.5 5v6h7V5" fill="none" stroke="#111322" stroke-width="1.1"/></svg></div>
    <div><svg width="12" height="12" viewBox="0 0 12 12"><path d="M1.5 4h9v2.5h-9zM2.5 6.5h7V11h-7zM6 4v7M6 4C4 1 2.5 3 6 4C8 1 9.5 3 6 4" fill="none" stroke="#111322" stroke-width="1"/></svg></div>
    <div><svg width="12" height="12" viewBox="0 0 12 12"><circle cx="6" cy="3.8" r="2.3" fill="none" stroke="#1634f2" stroke-width="1"/><path d="M1.8 11a4.2 4.2 0 0 1 8.4 0" fill="none" stroke="#1634f2" stroke-width="1"/></svg>PROFILE</div>
  </nav>
</section>
<p class="label" style="left:480px;top:2175px">Profile</p>

</body>
</html>
```